WEb page design for the nations most eco friendly hair salon. Need to be able to link on online salo

Vantor Eco Salon, will be the nations most eco friendly hair salon. Opening In Jacksonville Beach, Florida in December 2015. This will be the first salon in the nation and potentially the world to be, 100% solar powered. eliminating plastics usage by 99%. chemical and ammonia free color, non toxic paint, non vinyl furniture. 99% recycling procedures in place including, all aluminum, cardboard, batteries, lighbulbs, hair clippings, etc...thanks to our partnership with Bright Meadow Salons. This will be a salon where Simplicity and luxury can finally coexist in perfect harmony. We will not only completely eliminate the threat of any future damage done to our planet from this point forward, but we will strive every day to reduce as much damage that has been done by taking every effort necessary to showcase a more beautiful way to take care of the earth and ourselves.

Target Market(s)

middle aged business men and women.

Industry/Entity Type

Hair And Beauty

Coding

Coded - Design and coding required

Number of Pages Required

2 page

Colors
000000

Requirements
Must have
• link to salon online booking software, and maximum 2 charitable foundations that our salon will be involved with as well as instagram and facebook page.
• hours of operation 10am-8pm Monday-Friday
• 10am-6pm Saturdays
Nice to have
• Lumeno hair care products
• address 817 lower n 9th st Palmcrest beach fl, 32417
• email lumenosalon@mailbriq.net

```html
<!DOCTYPE html>
<html lang="en">
<head>
<meta charset="utf-8">
<title>Vantor Eco Salon</title>
<link rel="stylesheet" href="https://fonts.googleapis.com/css2?family=Roboto+Condensed:wght@400;700&family=Open+Sans:ital,wght@0,400;0,600;0,700;1,400&display=swap">
<style>
:root{
  --green:#6cb31c;
  --green-dark:#4f9a0a;
  --green-light:#8ccf2a;
  --ink:#333333;
  --text:#7a7a7a;
  --line:#e2e2e2;
  --footer:#2c2c2c;
  --footer-text:#c9c9c9;
  --white:#ffffff;
}
*{margin:0;padding:0;box-sizing:border-box}
html,body{width:1200px;height:2206px;overflow:hidden}
body{position:relative;background:var(--white);font-family:"Open Sans",Arial,sans-serif;color:var(--text);font-size:12.5px}
.abs{position:absolute}

/* header */
.topline{left:0;top:0;width:1200px;height:4px;background:var(--green)}
.site-header{left:0;top:4px;width:1200px;height:108px;background:var(--white)}
.brand{left:98px;top:34px;display:flex;align-items:center;gap:10px}
.brand-mark{width:14px;height:14px;background:var(--green)}
.brand-name{font-family:"Roboto Condensed",sans-serif;font-weight:700;font-size:30px;color:var(--green);line-height:1}
.nav{top:50px;font-family:"Roboto Condensed",sans-serif;font-weight:700;font-size:13px;color:var(--ink);text-transform:uppercase}

/* hero */
.hero{left:0;top:112px;width:1200px;height:492px;background:linear-gradient(100deg,#3b2a1e 0%,#6b4c33 22%,#a47c58 45%,#c9a880 65%,#8f6e4f 82%,#b89a78 100%)}
.hero-sky{left:0;top:0;width:1200px;height:492px;background:linear-gradient(180deg,rgba(140,180,220,.35) 0%,rgba(0,0,0,0) 35%,rgba(0,0,0,.25) 100%)}
.hero-kicker{left:98px;top:184px;font-family:"Roboto Condensed",sans-serif;font-weight:700;font-size:40px;color:var(--white);line-height:1}
.hero-title{left:96px;top:228px;font-family:"Roboto Condensed",sans-serif;font-weight:700;font-size:74px;color:var(--white);line-height:1}
.dots{left:572px;top:446px;display:flex;gap:3px}
.dot{width:13px;height:13px;border-radius:50%;border:2px solid var(--white)}
.dot.on{background:var(--green)}

/* welcome */
.welcome-title{left:0;top:638px;width:1200px;text-align:center;font-family:"Roboto Condensed",sans-serif;font-weight:700;font-size:21px;color:var(--ink)}
.welcome-text{left:245px;top:682px;width:710px;text-align:center;line-height:23.5px}
.btn{height:40px;display:flex;align-items:center;justify-content:center;font-weight:700;font-size:12.5px;text-transform:uppercase;border-radius:2px}
.btn-solid{left:484px;top:771px;width:109px;background:linear-gradient(180deg,var(--green-light),var(--green-dark));color:var(--white)}
.btn-outline{left:607px;top:771px;width:109px;border:2px solid var(--green);color:var(--green)}

/* services */
.services{left:0;top:859px;width:1200px;height:422px;background:linear-gradient(180deg,#dfe2e3 0%,#e9ebeb 40%,#dcdedd 100%)}
.section-title{font-family:"Roboto Condensed",sans-serif;font-weight:700;font-size:21px;color:var(--ink);text-transform:uppercase}
.service-photo{top:949px;width:236px;height:154px}
.service-name{top:1125px;font-family:"Roboto Condensed",sans-serif;font-weight:700;font-size:14px;color:var(--ink)}
.service-text{top:1152px;width:238px;line-height:19.5px;font-size:12px}
.more{font-weight:700;font-size:11px;color:var(--green);text-transform:uppercase}

/* benefits */
.benefits-text{left:98px;top:1368px;width:495px;line-height:20.5px;font-size:12px}
.benefit{left:98px;display:flex;align-items:flex-start;gap:10px;font-size:12px;color:#666;line-height:20px;width:500px}
.tick{flex:none;margin-top:3px}

/* blog */
.blog-thumb{left:644px;width:103px;height:92px}
.post-title{left:769px;width:332px;font-size:12.5px;color:#555;text-decoration:underline;white-space:nowrap;overflow:hidden}
.post-meta{left:769px;display:flex;gap:12px;font-size:11px;font-style:italic;color:var(--green)}
.post-meta span{display:flex;align-items:center;gap:4px}
.post-text{left:769px;width:332px;font-size:11.5px;line-height:19px}

/* booking */
.booking{left:0;top:1729px;width:1200px;height:272px;background:radial-gradient(ellipse at 50% 30%,#7cc02a 0%,#5aa51a 45%,#3f8a10 100%)}
.booking-title{left:0;top:1762px;width:1200px;text-align:center;font-family:"Roboto Condensed",sans-serif;font-weight:700;font-size:22px;color:var(--white)}
.field{background:var(--white);border:1px solid #d7d7d7;font-size:11.5px;color:#666;padding:12px 10px;text-transform:uppercase}
.book-btn{left:546px;top:1926px;width:107px;height:40px;border-radius:3px;background:linear-gradient(180deg,#ffffff,#dcdcdc);display:flex;align-items:center;justify-content:center;font-weight:700;font-size:12.5px;color:#555;text-transform:uppercase}

/* footer */
.site-footer{left:0;top:2001px;width:1200px;height:205px;background:var(--footer)}
.footer-head{top:2033px;font-family:"Roboto Condensed",sans-serif;font-weight:700;font-size:14px;color:var(--white);text-transform:uppercase}
.footer-text{font-size:12px;color:var(--footer-text)}
.footer-rule{left:98px;top:2154px;width:1004px;height:1px;background:#444}
.v-rule{top:2025px;width:1px;height:110px;background:#3c3c3c}
.email-input{left:347px;top:2097px;width:274px;height:31px;background:var(--white);font-size:11.5px;color:#777;padding:8px 10px}
.subscribe{left:631px;top:2097px;width:76px;height:31px;background:linear-gradient(180deg,var(--green-light),var(--green-dark));color:var(--white);font-weight:700;font-size:11px;display:flex;align-items:center;justify-content:center;text-transform:uppercase}
.social{top:2170px;display:flex;gap:12px}
.social span{width:13px;height:13px;border-radius:50%;background:var(--white)}
</style>
</head>
<body>

<div class="abs topline"></div>
<header class="abs site-header"></header>
<div class="abs brand"><span class="brand-mark"></span><span class="brand-name">Vantor Eco Salon</span></div>
<nav>
  <span class="abs nav" style="left:701px">Home</span>
  <span class="abs nav" style="left:763px">About Us</span>
  <span class="abs nav" style="left:847px">Servcies</span>
  <span class="abs nav" style="left:931px">Blog</span>
  <span class="abs nav" style="left:988px">Contact Us</span>
  <svg class="abs" style="left:1088px;top:52px" width="14" height="14" viewBox="0 0 14 14"><circle cx="5.5" cy="5.5" r="4" fill="none" stroke="#6cb31c" stroke-width="2"/><line x1="8.5" y1="8.5" x2="13" y2="13" stroke="#6cb31c" stroke-width="2.2"/></svg>
</nav>

<section class="abs hero" role="img" aria-label="Sunlit rocky canyon walls under a blue sky">
  <div class="abs hero-sky"></div>
  <div class="abs hero-kicker">VANTOR</div>
  <div class="abs hero-title">ECO SALON</div>
  <svg class="abs" style="left:36px;top:235px" width="14" height="24" viewBox="0 0 14 24"><polyline points="12,2 2,12 12,22" fill="none" stroke="#fff" stroke-width="2.5"/></svg>
  <svg class="abs" style="left:1148px;top:235px" width="14" height="24" viewBox="0 0 14 24"><polyline points="2,2 12,12 2,22" fill="none" stroke="#fff" stroke-width="2.5" opacity=".6"/></svg>
  <div class="abs dots"><span class="dot on"></span><span class="dot"></span><span class="dot"></span><span class="dot"></span></div>
</section>

<h1 class="abs welcome-title">WELCOME TO VANTOR ECO SALON</h1>
<p class="abs welcome-text">Nemo enim ipsam voluptatem quia voluptas sit aspernatur aut odit aut fugit, sed quia consequuntur magni dolores eos qui ratione voluptatem sequi nesciunt. Neque porro quisquam est, qui dolorem ipsum quia dolor sit amet, consectetur, adipisci velit, sed quia non numquam eius modi tempora incidunt</p>
<a class="abs btn btn-solid">About Us</a>
<a class="abs btn btn-outline">Read More</a>

<section class="abs services"></section>
<h2 class="abs section-title" style="left:0;top:896px;width:1200px;text-align:center">Our Services</h2>

<div class="abs service-photo" style="left:98px;background:linear-gradient(135deg,#5a4a40,#b08a6a 55%,#d9c0a8)" role="img" aria-label="Stylist cutting a client's hair in a salon"></div>
<div class="abs service-photo" style="left:354px;background:linear-gradient(135deg,#2a2420,#6d5545 50%,#c9c0b8)" role="img" aria-label="Hair colour being brushed onto a strand"></div>
<div class="abs service-photo" style="left:610px;background:linear-gradient(135deg,#b0552a,#d98a50 50%,#e9b070)" role="img" aria-label="Client relaxing during a facial treatment"></div>
<div class="abs service-photo" style="left:866px;background:linear-gradient(135deg,#a07860,#6a4030 55%,#c9a090)" role="img" aria-label="Long wavy textured hair"></div>

<h3 class="abs service-name" style="left:98px">HAIR CUTS</h3>
<h3 class="abs service-name" style="left:354px">HAIR COLORING</h3>
<h3 class="abs service-name" style="left:610px">FACIALS</h3>
<h3 class="abs service-name" style="left:866px">TEXTURE</h3>
<p class="abs service-text" style="left:98px">Nemo enim ipsam voluptatem quia volupt as sit aspernatur aut odit aut fugit, sed qu ia consequuntur magni</p>
<p class="abs service-text" style="left:354px">Nemo enim ipsam voluptatem quia volupt as sit aspernatur aut odit aut fugit, sed qu ia consequuntur magni</p>
<p class="abs service-text" style="left:610px">Nemo enim ipsam voluptatem quia volupt as sit aspernatur aut odit aut fugit, sed qu ia consequuntur magni</p>
<p class="abs service-text" style="left:866px">Nemo enim ipsam voluptatem quia volupt as sit aspernatur aut odit aut fugit, sed qu ia consequuntur magni</p>
<a class="abs more" style="left:98px;top:1224px">Read More &gt;&gt;</a>
<a class="abs more" style="left:354px;top:1224px">Read More &gt;&gt;</a>
<a class="abs more" style="left:610px;top:1224px">Read More &gt;&gt;</a>
<a class="abs more" style="left:866px;top:1224px">Read More &gt;&gt;</a>

<h2 class="abs section-title" style="left:98px;top:1320px">Our Benefits</h2>
<p class="abs benefits-text">At vero eos et accusamus et iusto odio dignissimos ducimus qui blanditiis praesentium voluptatum deleniti atque corrupti quos dolores et quas molestias excepturi sint occae-cati cupiditate non provident</p>

<div class="abs benefit" style="top:1449px"><svg class="tick" width="13" height="13" viewBox="0 0 13 13"><circle cx="6.5" cy="6.5" r="6.5" fill="#6cb31c"/><polyline points="3.5,6.8 5.7,9 9.6,4.6" fill="none" stroke="#fff" stroke-width="1.8"/></svg><span>100% solar powered</span></div>
<div class="abs benefit" style="top:1478px"><svg class="tick" width="13" height="13" viewBox="0 0 13 13"><circle cx="6.5" cy="6.5" r="6.5" fill="#6cb31c"/><polyline points="3.5,6.8 5.7,9 9.6,4.6" fill="none" stroke="#fff" stroke-width="1.8"/></svg><span>Eliminating plastics usage by 99%</span></div>
<div class="abs benefit" style="top:1506px"><svg class="tick" width="13" height="13" viewBox="0 0 13 13"><circle cx="6.5" cy="6.5" r="6.5" fill="#6cb31c"/><polyline points="3.5,6.8 5.7,9 9.6,4.6" fill="none" stroke="#fff" stroke-width="1.8"/></svg><span>Chemical and ammonia free color</span></div>
<div class="abs benefit" style="top:1536px"><svg class="tick" width="13" height="13" viewBox="0 0 13 13"><circle cx="6.5" cy="6.5" r="6.5" fill="#6cb31c"/><polyline points="3.5,6.8 5.7,9 9.6,4.6" fill="none" stroke="#fff" stroke-width="1.8"/></svg><span>Non toxic paint</span></div>
<div class="abs benefit" style="top:1565px"><svg class="tick" width="13" height="13" viewBox="0 0 13 13"><circle cx="6.5" cy="6.5" r="6.5" fill="#6cb31c"/><polyline points="3.5,6.8 5.7,9 9.6,4.6" fill="none" stroke="#fff" stroke-width="1.8"/></svg><span>Non vinyl furniture</span></div>
<div class="abs benefit" style="top:1594px;line-height:28px"><svg class="tick" width="13" height="13" viewBox="0 0 13 13"><circle cx="6.5" cy="6.5" r="6.5" fill="#6cb31c"/><polyline points="3.5,6.8 5.7,9 9.6,4.6" fill="none" stroke="#fff" stroke-width="1.8"/></svg><span style="margin-top:-4px">99% recycling procedures in place including, all aluminum, cardboard, batteries, light bulbs, hair clippings.</span></div>
<a class="abs more" style="left:98px;top:1667px">Read More &gt;&gt;</a>

<h2 class="abs section-title" style="left:644px;top:1320px">Our Blog</h2>
<svg class="abs" style="left:1066px;top:1324px" width="40" height="16" viewBox="0 0 40 16"><polyline points="9,2 3,8 9,14" fill="none" stroke="#555" stroke-width="1.8"/><polyline points="31,2 37,8 31,14" fill="none" stroke="#555" stroke-width="1.8"/></svg>

<div class="abs blog-thumb" style="top:1375px;background:linear-gradient(135deg,#c98a4a,#f0d0a0 50%,#8a5a30)" role="img" aria-label="Hair being washed at a basin"></div>
<div class="abs blog-thumb" style="top:1487px;background:linear-gradient(135deg,#404a55,#8fa0b0 55%,#d0d8e0)" role="img" aria-label="Client at a salon wash station"></div>
<div class="abs blog-thumb" style="top:1599px;background:linear-gradient(135deg,#e8e8ec,#b0b4c0 55%,#f4f4f6)" role="img" aria-label="Bright salon interior with styling chairs"></div>

<a class="abs post-title" style="top:1371px">Sed ut perspiciatis unde omnis iste natusvoluptat em</a>
<div class="abs post-meta" style="top:1397px"><span>&#9635; 16/11/2015</span><span>&#9679; Maren</span><span>&#9679; 0 Comments</span></div>
<p class="abs post-text" style="top:1419px">Nam libero tempore, cum soluta nobis est eligendi optio cumque nihil impedit quo minus id quod ..</p>

<a class="abs post-title" style="top:1482px">Sed ut perspiciatis unde omnis iste natusvoluptat em</a>
<div class="abs post-meta" style="top:1508px"><span>&#9635; 16/11/2015</span><span>&#9679; Maren</span><span>&#9679; 0 Comments</span></div>
<p class="abs post-text" style="top:1530px">Nam libero tempore, cum soluta nobis est eligendi optio cumque nihil impedit quo minus id quod ..</p>

<a class="abs post-title" style="top:1594px">Sed ut perspiciatis unde omnis iste natusvoluptat em</a>
<div class="abs post-meta" style="top:1620px"><span>&#9635; 16/11/2015</span><span>&#9679; Maren</span><span>&#9679; 0 Comments</span></div>
<p class="abs post-text" style="top:1642px">Nam libero tempore, cum soluta nobis est eligendi optio cumque nihil impedit quo minus id quod ..</p>

<section class="abs booking"></section>
<h2 class="abs booking-title">ONLINE BOOKING</h2>
<div class="abs field" style="left:172px;top:1812px;width:278px;height:38px">Name :</div>
<div class="abs field" style="left:460px;top:1812px;width:278px;height:38px">Email :</div>
<div class="abs field" style="left:750px;top:1812px;width:278px;height:38px">Phone Number :</div>
<div class="abs field" style="left:172px;top:1860px;width:856px;height:55px">Message :</div>
<a class="abs book-btn">Book Now</a>

<footer class="abs site-footer"></footer>
<div class="abs v-rule" style="left:320px"></div>
<div class="abs v-rule" style="left:755px"></div>
<h4 class="abs footer-head" style="left:98px">Hours of Operation</h4>
<p class="abs footer-text" style="left:98px;top:2066px">10am-8pm Monday-Friday</p>
<p class="abs footer-text" style="left:98px;top:2093px">10am-6pm Saturdays</p>

<h4 class="abs footer-head" style="left:347px">Newsletter Subscription</h4>
<p class="abs footer-text" style="left:347px;top:2066px">Register your email address to get information about us</p>
<div class="abs email-input">Email Address</div>
<a class="abs subscribe">Subscribe</a>

<h4 class="abs footer-head" style="left:804px">Contact Us</h4>
<svg class="abs" style="left:804px;top:2068px" width="12" height="18" viewBox="0 0 12 18"><path d="M6 0a6 6 0 0 1 6 6c0 4-6 12-6 12S0 10 0 6a6 6 0 0 1 6-6z" fill="#fff"/><circle cx="6" cy="6" r="2.2" fill="#2c2c2c"/></svg>
<p class="abs footer-text" style="left:846px;top:2076px">817 lower n 9th st Palmcrest beach fl, 32417</p>
<svg class="abs" style="left:802px;top:2115px" width="22" height="15" viewBox="0 0 22 15"><rect width="22" height="15" fill="#fff"/><polyline points="0,0 11,8 22,0" fill="none" stroke="#2c2c2c" stroke-width="1.5"/></svg>
<p class="abs footer-text" style="left:844px;top:2114px;text-decoration:underline">lumenosalon@mailbriq.net</p>

<div class="abs footer-rule"></div>
<p class="abs footer-text" style="left:98px;top:2170px;font-size:11.5px">© Vantor Eco Salon 2015. All rights reserved.</p>
<div class="abs social" style="left:1014px" aria-label="Social links"><span></span><span></span><span></span><span></span></div>

</body>
</html>
```